Pet Product Manufacturer needs Catalogue Design

We need a catalogue design (double sided information sheet) for a manufacturer of embroidered pet feeding mats to use to send to upscale boutique pet stores to introduce them to the product. The design should relate to our website TailTableLinens.com. The sheet should include green with pink polkadots to coordinate with the packaging and branding. We would like a separate coordinated order form that can be faxed or emailed.
Updates

Project Deadline Extended
Reason: need revisions and order form

Project Deadline Extended
Reason: Waiting for revised files

Target Market(s)

Upscale pet boutique owner.

Industry/Entity Type

Boutique

Requirements
Must have
• 2 sided or 2 page brochure
order form
green and pink polka dots and logo
4-6 Photographs of sample mats
Since the pet stores can choose their mat sizes, the colors, the embroidery threads and the embroidery style there must be areas to show the mat and thread color choices and the embroidery options.
See www.TailTableLinenscom for colors, threads and embroidery choices.
Do NOT include the custom name personalization. This catalog is for wholesale orders.

Nice to have
• This brochure is for store owners, not the actual consumers so it would be great to have a "suggested starter pack" area so that it is clear how to order.

It would be nice to have the cat mat info in this piece too, however it may be easier to only focus on the dogs.

```html
<!DOCTYPE html>
<html lang="en">
<head>
<meta charset="utf-8">
<title>Order Form – Tail Table Linens</title>
<link href="https://fonts.googleapis.com/css2?family=Arimo:wght@400;700&display=swap" rel="stylesheet">
<style>
:root{
  --green:#8cc63f;
  --green-text:#7ac143;
  --pink:#e5177b;
  --ink:#222;
  --band-dark:#231f20;
  --line:#333;
  --field:#999;
  --backdrop:#e9e6e2;
  --paper:#fff;
}
*{box-sizing:border-box;margin:0;padding:0}
html,body{width:1200px;height:813px;overflow:hidden;background:var(--backdrop);font-family:"Arimo",Arial,sans-serif;color:var(--ink)}
.sheet{position:absolute;top:38px;width:572px;height:740px;background:var(--paper);box-shadow:0 2px 8px rgba(0,0,0,.35)}
.sheet--front{left:14px}
.sheet--back{left:612px}
.band-dark{position:absolute;left:0;right:0;top:0;height:57px;background:var(--band-dark)}
.band-pink{position:absolute;left:0;right:0;top:57px;height:270px;background:var(--pink)}
.frame{position:absolute;left:14px;top:10px;width:544px;height:714px;background:var(--green);box-shadow:0 2px 5px rgba(0,0,0,.3)}
.frame-inner{position:absolute;left:12px;top:14px;right:16px;bottom:12px;background:var(--paper)}
.abs{position:absolute}
.title{font-size:20px;font-weight:700;color:var(--green-text);top:62px}
.brand{left:290px;top:45px;width:250px;height:61px;border:1.5px solid var(--pink);display:flex;align-items:center;gap:12px;padding-left:12px}
.brand-mark{width:40px;height:40px;background:var(--green)}
.brand-name{font-size:16px;color:var(--ink);letter-spacing:.3px}
.sheet--back .brand{left:284px}
.section-head{font-size:10.5px;font-weight:700;color:var(--pink);left:45px;top:106px}
.field-label{left:45px;font-size:10px}
.field{left:146px;width:394px;height:20px;border:1px solid var(--field)}
.pick-label{left:44px;font-size:9.5px;color:var(--pink)}
.swatches{left:44px;display:flex;gap:4.6px}
.swatch{width:20px;text-align:center;font-size:5px;line-height:6px;color:#555}
.swatch i{display:block;width:20px;height:15px;margin-bottom:2px;border:1px solid #ddd}
.rule{left:44px;width:496px;height:1px;background:#bbb}
.monograms{left:158px;top:342px;display:flex;gap:3px}
.monogram{width:38px;height:38px;background:#cfcfcf;border:1px solid #888}
.order-table{border-collapse:collapse;table-layout:fixed}
.order-table th{color:var(--pink);font-size:10px;font-weight:700;height:20px;border:1px solid var(--line);border-top-width:2px;text-align:center}
.order-table th small{font-size:7px}
.order-table td{height:20px;border:1px solid var(--line)}
.order-table tr td:first-child,.order-table tr th:first-child{border-left-width:2px}
.order-table tr td:last-child,.order-table tr th:last-child{border-right-width:2px}
.order-table tr:last-child td{border-bottom-width:2px}
.blurb{left:43px;top:673px;font-size:5.6px;color:#555}
.footer{left:43px;top:690px;width:498px;display:flex;justify-content:space-between;font-size:11px;font-weight:700;color:var(--green-text)}
.footer span+span{border-left:1.5px solid var(--green);padding-left:28px}
</style>
</head>
<body>

<section class="sheet sheet--front">
  <div class="band-dark"></div><div class="band-pink"></div>
  <div class="frame" role="img" aria-label="Green border with pink polka dots"><div class="frame-inner"></div></div>

  <h1 class="abs title" style="left:43px">ORDER FORM</h1>
  <div class="abs brand"><span class="brand-mark"></span><span class="brand-name">TAIL TABLE LINENS</span></div>

  <h2 class="abs section-head">CUSTOMER INFORMATION</h2>
  <span class="abs field-label" style="top:128px">Customer Name :</span><span class="abs field" style="top:125px"></span>
  <span class="abs field-label" style="top:152px">Shipping Address:</span><span class="abs field" style="top:149px"></span>
  <span class="abs field-label" style="top:176px">Contact Name:</span><span class="abs field" style="top:173px"></span>
  <span class="abs field-label" style="top:200px">Phone:</span><span class="abs field" style="top:197px"></span>

  <span class="abs pick-label" style="top:221px">Mat color:</span>
  <div class="abs swatches" style="top:238px">
    <div class="swatch"><i style="background:#231f20"></i>black</div>
    <div class="swatch"><i style="background:#2b4a9a"></i>dark blue</div>
    <div class="swatch"><i style="background:#4a2a22"></i>dark brown</div>
    <div class="swatch"><i style="background:#7a2434"></i>bur-gundy</div>
    <div class="swatch"><i style="background:#2e6b56"></i>forest green</div>
    <div class="swatch"><i style="background:#7a7a7a"></i>gray</div>
    <div class="swatch"><i style="background:#0f7b73"></i>teal green</div>
    <div class="swatch"><i style="background:#eab4d2"></i>light laven-der</div>
    <div class="swatch"><i style="background:#1eb3df"></i>light blue</div>
    <div class="swatch"><i style="background:#2fb8b4"></i>light green</div>
    <div class="swatch"><i style="background:#9c7bb8"></i>light purple</div>
    <div class="swatch"><i style="background:#6a8c3c"></i>olive green</div>
    <div class="swatch"><i style="background:#f28a2c"></i>orange</div>
    <div class="swatch"><i style="background:#ec4c86"></i>pink</div>
    <div class="swatch"><i style="background:#4b3a8a"></i>dark purple</div>
    <div class="swatch"><i style="background:#e22d2d"></i>red</div>
    <div class="swatch"><i style="background:#3f5560"></i>slate blue</div>
    <div class="swatch"><i style="background:#fff"></i>white</div>
    <div class="swatch"><i style="background:#f5c93a"></i>yellow</div>
    <div class="swatch"><i style="background:#8fcac3"></i>seafoam</div>
  </div>
  <div class="abs rule" style="top:277px"></div>

  <span class="abs pick-label" style="top:282px">Thread color:</span>
  <div class="abs swatches" style="top:298px">
    <div class="swatch"><i style="background:#6ba86b"></i>spring</div>
    <div class="swatch"><i style="background:#2d3a4e"></i>navy</div>
    <div class="swatch"><i style="background:#2a7fb8"></i>academy</div>
    <div class="swatch"><i style="background:#1e8fae"></i>tur-quoise</div>
    <div class="swatch"><i style="background:#9fc0d8"></i>baby blue</div>
    <div class="swatch"><i style="background:#c0213a"></i>valentine</div>
    <div class="swatch"><i style="background:#c83a7a"></i>pinky</div>
    <div class="swatch"><i style="background:#eea0b8"></i>baby pink</div>
    <div class="swatch"><i style="background:#ef553a"></i>tan-gerine</div>
    <div class="swatch"><i style="background:#f3b05a"></i>mustard</div>
    <div class="swatch"><i style="background:#f6d36a"></i>sun-shine</div>
    <div class="swatch"><i style="background:#4e3a7a"></i>purple</div>
    <div class="swatch"><i style="background:#cfbfa8"></i>khaki</div>
    <div class="swatch"><i style="background:#1aa063"></i>preppy</div>
    <div class="swatch"><i style="background:#8f8cb8"></i>laven-der</div>
    <div class="swatch"><i style="background:#5e4236"></i>brown</div>
    <div class="swatch"><i style="background:#111"></i>black</div>
    <div class="swatch"><i style="background:#fff"></i>white</div>
  </div>
  <div class="abs rule" style="top:332px"></div>

  <span class="abs pick-label" style="top:341px">Choose a monogram style:</span>
  <div class="abs monograms">
    <div class="monogram" role="img" aria-label="Paw prints embroidery style"></div>
    <div class="monogram" role="img" aria-label="Woof lettering embroidery style"></div>
    <div class="monogram" role="img" aria-label="Friends fur-ever lettering embroidery style"></div>
    <div class="monogram" role="img" aria-label="Talk to the tail lettering embroidery style"></div>
    <div class="monogram" role="img" aria-label="I love my dog lettering embroidery style"></div>
  </div>

  <table class="abs order-table" style="left:35px;top:400px;width:503px">
    <thead><tr><th>Quantity</th><th>Mat (Dog/Cat)</th><th>Mat Size <small>(S, M, L)</small></th><th>Mat Color</th><th>Design</th><th>Thread Color</th></tr></thead>
    <tbody>
      <tr><td></td><td></td><td></td><td></td><td></td><td></td></tr>
      <tr><td></td><td></td><td></td><td></td><td></td><td></td></tr>
      <tr><td></td><td></td><td></td><td></td><td></td><td></td></tr>
      <tr><td></td><td></td><td></td><td></td><td></td><td></td></tr>
      <tr><td></td><td></td><td></td><td></td><td></td><td></td></tr>
      <tr><td></td><td></td><td></td><td></td><td></td><td></td></tr>
      <tr><td></td><td></td><td></td><td></td><td></td><td></td></tr>
      <tr><td></td><td></td><td></td><td></td><td></td><td></td></tr>
      <tr><td></td><td></td><td></td><td></td><td></td><td></td></tr>
      <tr><td></td><td></td><td></td><td></td><td></td><td></td></tr>
      <tr><td></td><td></td><td></td><td></td><td></td><td></td></tr>
      <tr><td></td><td></td><td></td><td></td><td></td><td></td></tr>
    </tbody>
  </table>

  <p class="abs blurb">The custom embroidered pet mats protect your floor under food and water bowls and give your treasured pet a place mat of their own.</p>
  <div class="abs footer"><span>www.TailTableLinens.com</span><span>Ph: 555-014-2230</span><span>Fax: 555-019-4471</span></div>
</section>

<section class="sheet sheet--back">
  <div class="band-dark"></div><div class="band-pink"></div>
  <div class="frame" role="img" aria-label="Green border with pink polka dots"><div class="frame-inner"></div></div>

  <h1 class="abs title" style="left:42px">ORDER FORM</h1>
  <div class="abs brand"><span class="brand-mark"></span><span class="brand-name">TAIL TABLE LINENS</span></div>

  <table class="abs order-table" style="left:33px;top:140px;width:502px">
    <thead><tr><th>Quantity</th><th>Mat (Dog/Cat)</th><th>Mat Size <small>(S, M, L)</small></th><th>Mat Color</th><th>Design</th><th>Thread Color</th></tr></thead>
    <tbody>
      <tr><td></td><td></td><td></td><td></td><td></td><td></td></tr>
      <tr><td></td><td></td><td></td><td></td><td></td><td></td></tr>
      <tr><td></td><td></td><td></td><td></td><td></td><td></td></tr>
      <tr><td></td><td></td><td></td><td></td><td></td><td></td></tr>
      <tr><td></td><td></td><td></td><td></td><td></td><td></td></tr>
      <tr><td></td><td></td><td></td><td></td><td></td><td></td></tr>
      <tr><td></td><td></td><td></td><td></td><td></td><td></td></tr>
      <tr><td></td><td></td><td></td><td></td><td></td><td></td></tr>
      <tr><td></td><td></td><td></td><td></td><td></td><td></td></tr>
      <tr><td></td><td></td><td></td><td></td><td></td><td></td></tr>
      <tr><td></td><td></td><td></td><td></td><td></td><td></td></tr>
      <tr><td></td><td></td><td></td><td></td><td></td><td></td></tr>
      <tr><td></td><td></td><td></td><td></td><td></td><td></td></tr>
      <tr><td></td><td></td><td></td><td></td><td></td><td></td></tr>
      <tr><td></td><td></td><td></td><td></td><td></td><td></td></tr>
      <tr><td></td><td></td><td></td><td></td><td></td><td></td></tr>
      <tr><td></td><td></td><td></td><td></td><td></td><td></td></tr>
      <tr><td></td><td></td><td></td><td></td><td></td><td></td></tr>
      <tr><td></td><td></td><td></td><td></td><td></td><td></td></tr>
      <tr><td></td><td></td><td></td><td></td><td></td><td></td></tr>
      <tr><td></td><td></td><td></td><td></td><td></td><td></td></tr>
      <tr><td></td><td></td><td></td><td></td><td></td><td></td></tr>
      <tr><td></td><td></td><td></td><td></td><td></td><td></td></tr>
      <tr><td></td><td></td><td></td><td></td><td></td><td></td></tr>
      <tr><td></td><td></td><td></td><td></td><td></td><td></td></tr>
    </tbody>
  </table>

  <p class="abs blurb" style="left:42px">The custom embroidered pet mats protect your floor under food and water bowls and give your treasured pet a place mat of their own.</p>
  <div class="abs footer" style="left:42px"><span>www.TailTableLinens.com</span><span>Ph: 555-014-2230</span><span>Fax: 555-019-4471</span></div>
</section>

</body>
</html>
```